Marrowdale PowerPoint Template

We would like a PowerPoint template created for our company to use as a basis for all our presentations (to make creating the presentations easier as well as create visual consistency). We are currently presenting online (using Zoom) but also anticipate doing live presentation with a large screen in the future. Around 15 different slides please.
We are a Succession and Estate Planning firm, working with Entrepreneurs and their families in Western Canada. We offer Advanced Insurance Solutions and Charitable Gifting Strategies that help you "Let Your Legacy Thrive".
Our logo colours are:
Green - R:131 G:194 B:66 or #83c242 or (54-0-99-0)
Dk Brown/Black - R:59 G:56 B:57 or #3b3839 or (68-63-60-53)
Grey - R:213 G:213 B:213 or #d5d5d5 or (15-12-12-0)
We are wanting something clean, uncluttered, professional, calm, perhaps using leaves/plants as a theme to represent financial growth over time. Please include some simple tables, graphs, circular process
In most of our presentations we're conveying:
-the transition of wealth to the next generation
-philanthropy
-saving
-building a legacy to continue long after you're gone
-Tax strategies
-Retirement
-Life Insurance
-Collaboration with other professionals

```html
<!DOCTYPE html>
<html lang="en">
<head>
<meta charset="utf-8">
<title>Marrowdale Presentation Template</title>
<link href="https://fonts.googleapis.com/css2?family=Open+Sans:wght@400;600;700&display=swap" rel="stylesheet">
<style>
:root{
  --green:#83c242;
  --green-dark:#5f9a2c;
  --ink:#3b3839;
  --grey:#d5d5d5;
  --text:#6b6869;
  --page:#eeeeee;
  --white:#ffffff;
}
*{margin:0;padding:0;box-sizing:border-box}
html,body{width:1200px;height:2192px;overflow:hidden;background:var(--page);font-family:"Open Sans",Arial,sans-serif;color:var(--text)}
.deck{position:relative;width:1200px;height:2192px}
.slide{position:absolute;width:490px;height:240px;background:var(--white);overflow:hidden;box-shadow:0 1px 4px rgba(0,0,0,.18)}
.col-l{left:40px}.col-r{left:670px}
.r1{top:38px}.r2{top:314px}.r3{top:590px}.r4{top:866px}.r5{top:1142px}.r6{top:1418px}.r7{top:1694px}.r8{top:1970px}
.brand{position:absolute;top:9px;right:14px;font-size:9px;font-weight:700;color:var(--green);display:flex;align-items:center;gap:4px}
.brand::before{content:"";width:7px;height:7px;border-radius:50%;background:var(--green)}
.brand.light{color:var(--white)}.brand.light::before{background:var(--white)}
.footer-rule{position:absolute;left:0;right:0;bottom:0;height:4px;background:linear-gradient(90deg,var(--green) 0 30%,var(--grey) 30% 100%)}
.photo{position:absolute}
.ph-sky{background:linear-gradient(180deg,#b9c1c4 0%,#7f8d92 55%,#3f4a4d 100%)}
.ph-sprout{background:radial-gradient(circle at 55% 40%,#9fd35a 0%,#5f8f33 35%,#2f3b26 75%)}
.ph-sunset{background:linear-gradient(180deg,#f1c98a 0%,#9aa7ae 50%,#33413f 100%)}
.ph-office{background:linear-gradient(135deg,#c9c4bc,#7d7770)}
.ph-forest{background:linear-gradient(160deg,#8fb36a,#3c5530)}
.ph-warm{background:linear-gradient(135deg,#e2b98c,#7a5a44)}
.ph-lake{background:linear-gradient(180deg,#c8d3d8,#5c7580)}
.title{position:absolute;color:var(--green);font-weight:700;font-size:18px;line-height:1.15}
.title.center{left:0;right:0;text-align:center}
.body{font-size:6.5px;line-height:1.5;color:var(--text)}
.abs{position:absolute}
.box{position:absolute;padding:9px 10px;color:var(--white)}
.box h4{font-size:8.5px;font-weight:700;margin-bottom:4px}
.box p{font-size:6px;line-height:1.5;opacity:.9}
.box.dark{background:var(--ink)}.box.green{background:var(--green)}
.item h4{font-size:8px;color:var(--ink);font-weight:700;margin:4px 0 3px}
.item p{font-size:6px;line-height:1.5}
.icon{width:22px;height:22px}
.list li{list-style:none;display:flex;align-items:center;gap:7px;font-size:8px;color:var(--ink);margin-bottom:9px}
.list li span{width:14px;height:14px;border-radius:50%;background:var(--green);flex:none}
.hero-word{position:absolute;left:30px;top:92px;font-size:34px;letter-spacing:9px;font-weight:600;color:var(--white)}
.doc{position:absolute;top:58px;width:96px;height:120px;border:1px solid var(--grey)}
.doc i{display:block;height:6px;margin:6px 8px 0;background:var(--grey)}
.doc i.g{background:var(--green)}
.cap{position:absolute;font-size:7px;font-weight:700;color:var(--ink);text-align:center}
.bar{position:absolute;height:18px;background:var(--green);color:var(--white);font-size:7.5px;font-weight:700;padding:4px 8px}
</style>
</head>
<body>
<main class="deck">

<!-- 1 cover -->
<section class="slide col-l r1">
  <div class="photo ph-sky" style="inset:0" role="img" aria-label="Misty lake landscape at dawn"></div>
  <div class="hero-word">MARROWDALE</div>
  <div class="brand light">Marrowdale</div>
</section>

<!-- 2 succession -->
<section class="slide col-r r1">
  <div class="photo ph-sprout" style="left:0;top:0;width:200px;height:240px" role="img" aria-label="Young green sprout growing from soil"></div>
  <div class="brand">Marrowdale</div>
  <h2 class="title" style="left:222px;top:40px">Succession<br>&amp; Estate Planning</h2>
  <p class="body abs" style="left:222px;top:95px;width:245px">We help entrepreneurs and their families plan the orderly transfer of the business and personal wealth they have built across generations.</p>
  <p class="body abs" style="left:222px;top:140px;width:245px">Our advisors bring together insurance, tax and charitable giving strategies so that your plan keeps working long after it is signed.</p>
  <div class="footer-rule"></div>
</section>

<!-- 3 expertise list -->
<section class="slide col-l r2">
  <div class="brand">Marrowdale</div>
  <h2 class="title" style="left:22px;top:50px">Our Expertise</h2>
  <ul class="list abs" style="left:22px;top:90px">
    <li><span></span>Estate Planning</li>
    <li><span></span>Business Succession Planning</li>
    <li><span></span>Philanthropic Planning</li>
    <li><span></span>Advanced Insurance Planning</li>
  </ul>
  <div class="photo ph-sprout" style="left:245px;top:30px;width:115px;height:98px" role="img" aria-label="Seedling in soil"></div>
  <div class="photo ph-office" style="left:365px;top:30px;width:115px;height:98px" role="img" aria-label="Advisor meeting with clients"></div>
  <div class="photo ph-lake" style="left:245px;top:133px;width:115px;height:98px" role="img" aria-label="Calm lake view"></div>
  <div class="photo ph-warm" style="left:365px;top:133px;width:115px;height:98px" role="img" aria-label="Family reviewing documents"></div>
</section>

<!-- 4 expertise banner -->
<section class="slide col-r r2">
  <div class="photo ph-forest" style="left:0;top:0;width:490px;height:95px" role="img" aria-label="Green leaves in sunlight"></div>
  <h2 class="title center" style="top:38px;color:var(--white)">Our Expertise</h2>
  <div class="brand light">Marrowdale</div>
  <div class="item abs" style="left:20px;top:108px;width:140px">
    <div class="photo ph-office" style="position:relative;height:50px" role="img" aria-label="Business meeting"></div>
    <h4>Estate Planning</h4><p>Protect and pass on the wealth you built with a clear plan.</p>
  </div>
  <div class="item abs" style="left:175px;top:108px;width:140px">
    <div class="photo ph-lake" style="position:relative;height:50px" role="img" aria-label="Quiet lake"></div>
    <h4>Succession Planning</h4><p>Prepare the next leaders of your business for a smooth handover.</p>
  </div>
  <div class="item abs" style="left:330px;top:108px;width:140px">
    <div class="photo ph-warm" style="position:relative;height:50px" role="img" aria-label="Family together"></div>
    <h4>Philanthropy</h4><p>Give to the causes you care about in a tax-smart way.</p>
  </div>
</section>

<!-- 5 expertise boxes -->
<section class="slide col-l r3">
  <div class="brand">Marrowdale</div>
  <h2 class="title center" style="top:22px">Our Expertise</h2>
  <div class="box dark" style="left:30px;top:58px;width:212px;height:82px"><h4>Estate Planning</h4><p>Structure your estate so assets pass on with less tax and delay.</p></div>
  <div class="box green" style="left:248px;top:58px;width:212px;height:82px"><h4>Business Succession</h4><p>Plan the exit, sale or family transfer of your company.</p></div>
  <div class="box green" style="left:30px;top:146px;width:212px;height:82px"><h4>Philanthropic Planning</h4><p>Build charitable gifting into your long-term strategy.</p></div>
  <div class="box dark" style="left:248px;top:146px;width:212px;height:82px"><h4>Advanced Insurance Solutions</h4><p>Use insurance to fund taxes and protect your legacy.</p></div>
</section>

<!-- 6 six options boxes -->
<section class="slide col-r r3">
  <div class="photo ph-sunset" style="left:0;top:0;width:150px;height:240px" role="img" aria-label="Sunset over water"></div>
  <div class="brand">Marrowdale</div>
  <h2 class="title" style="left:168px;top:26px">Six options explained</h2>
  <div class="box dark" style="left:168px;top:62px;width:96px;height:78px"><h4>Write the option here</h4><p>Short text about this option.</p></div>
  <div class="box green" style="left:270px;top:62px;width:96px;height:78px"><h4>Write the option here</h4><p>Short text about this option.</p></div>
  <div class="box dark" style="left:372px;top:62px;width:96px;height:78px"><h4>Write the option here</h4><p>Short text about this option.</p></div>
  <div class="box green" style="left:168px;top:146px;width:96px;height:78px"><h4>Write the option here</h4><p>Short text about this option.</p></div>
  <div class="box dark" style="left:270px;top:146px;width:96px;height:78px"><h4>Write the option here</h4><p>Short text about this option.</p></div>
  <div class="box green" style="left:372px;top:146px;width:96px;height:78px"><h4>Write the option here</h4><p>Short text about this option.</p></div>
</section>

<!-- 7 process -->
<section class="slide col-l r4">
  <div class="brand">Marrowdale</div>
  <h2 class="title center" style="top:22px">Integrated Planning Process</h2>
  <div class="photo" style="left:185px;top:58px;width:120px;height:165px;background:radial-gradient(ellipse at 50% 35%,#5c5a5b 0%,#3b3839 45%,transparent 72%)" role="img" aria-label="Tree illustration with spreading branches"></div>
  <div class="item abs" style="left:30px;top:70px;width:130px"><h4>Step 1: Analysis</h4><p>Review your goals, assets and family needs.</p></div>
  <div class="item abs" style="left:30px;top:145px;width:130px"><h4>Step 3: Implementation</h4><p>Put the agreed plan into action.</p></div>
  <div class="item abs" style="left:330px;top:70px;width:130px"><h4>Step 2: Recommendations</h4><p>Present clear options for your plan.</p></div>
  <div class="item abs" style="left:330px;top:145px;width:130px"><h4>Step 4: Review</h4><p>Revisit the plan as life changes.</p></div>
</section>

<!-- 8 three options -->
<section class="slide col-r r4">
  <div class="brand">Marrowdale</div>
  <h2 class="title center" style="top:26px">Three options explained</h2>
  <div class="item abs" style="left:30px;top:80px;width:130px;text-align:center">
    <svg class="icon" viewBox="0 0 24 24"><circle cx="12" cy="12" r="10" fill="none" stroke="#3b3839" stroke-width="2"/><path d="M12 6v6l4 3" stroke="#83c242" stroke-width="2" fill="none"/></svg>
    <h4>Write the option here</h4><p>Short supporting text for the first option.</p></div>
  <div class="item abs" style="left:180px;top:80px;width:130px;text-align:center">
    <svg class="icon" viewBox="0 0 24 24"><rect x="3" y="3" width="18" height="18" rx="2" fill="none" stroke="#3b3839" stroke-width="2"/><path d="M7 12l3 3 7-7" stroke="#83c242" stroke-width="2" fill="none"/></svg>
    <h4>Write the option here</h4><p>Short supporting text for the second option.</p></div>
  <div class="item abs" style="left:330px;top:80px;width:130px;text-align:center">
    <svg class="icon" viewBox="0 0 24 24"><path d="M6 3h12M6 21h12M7 3c0 6 10 6 10 9s-10 3-10 9M17 3c0 6-10 6-10 9" stroke="#3b3839" stroke-width="2" fill="none"/></svg>
    <h4>Write the option here</h4><p>Short supporting text for the third option.</p></div>
  <div class="footer-rule"></div>
</section>

<!-- 9 six options icons -->
<section class="slide col-l r5">
  <div class="brand">Marrowdale</div>
  <h2 class="title" style="left:30px;top:24px">Six options explained</h2>
  <div class="item abs" style="left:30px;top:68px;width:130px"><svg class="icon" viewBox="0 0 24 24"><circle cx="12" cy="12" r="9" fill="#83c242"/></svg><h4>Write the option here</h4><p>Short text about this option.</p></div>
  <div class="item abs" style="left:180px;top:68px;width:130px"><svg class="icon" viewBox="0 0 24 24"><circle cx="12" cy="12" r="9" fill="#3b3839"/></svg><h4>Write the option here</h4><p>Short text about this option.</p></div>
  <div class="item abs" style="left:330px;top:68px;width:130px"><svg class="icon" viewBox="0 0 24 24"><circle cx="12" cy="12" r="9" fill="#83c242"/></svg><h4>Write the option here</h4><p>Short text about this option.</p></div>
  <div class="item abs" style="left:30px;top:150px;width:130px"><svg class="icon" viewBox="0 0 24 24"><circle cx="12" cy="12" r="9" fill="#3b3839"/></svg><h4>Write the option here</h4><p>Short text about this option.</p></div>
  <div class="item abs" style="left:180px;top:150px;width:130px"><svg class="icon" viewBox="0 0 24 24"><circle cx="12" cy="12" r="9" fill="#83c242"/></svg><h4>Write the option here</h4><p>Short text about this option.</p></div>
  <div class="item abs" style="left:330px;top:150px;width:130px"><svg class="icon" viewBox="0 0 24 24"><circle cx="12" cy="12" r="9" fill="#3b3839"/></svg><h4>Write the option here</h4><p>Short text about this option.</p></div>
</section>

<!-- 10 three themes -->
<section class="slide col-r r5">
  <div class="brand">Marrowdale</div>
  <h2 class="title center" style="top:24px">3 themes with images</h2>
  <div class="item abs" style="left:30px;top:62px;width:134px"><div class="photo ph-warm" style="position:relative;height:78px" role="img" aria-label="Couple planning at home"></div><h4>Write the theme here</h4><p>Short text about this theme.</p></div>
  <div class="item abs" style="left:178px;top:62px;width:134px"><div class="photo ph-lake" style="position:relative;height:78px" role="img" aria-label="Lake landscape"></div><h4>Write the theme here</h4><p>Short text about this theme.</p></div>
  <div class="item abs" style="left:326px;top:62px;width:134px"><div class="photo ph-office" style="position:relative;height:78px" role="img" aria-label="Advisors at a desk"></div><h4>Write the theme here</h4><p>Short text about this theme.</p></div>
</section>

<!-- 11 section title -->
<section class="slide col-l r6">
  <div class="photo ph-sunset" style="left:0;top:0;width:490px;height:182px" role="img" aria-label="Sun rising over a lake"></div>
  <div class="brand light">Marrowdale</div>
  <h2 class="title center" style="top:192px;font-size:16px">Your Title slide here</h2>
  <p class="body abs" style="left:0;right:0;top:215px;text-align:center">Add a short subtitle that introduces this section</p>
</section>

<!-- 12 documents -->
<section class="slide col-r r6">
  <div class="brand">Marrowdale</div>
  <h2 class="title center" style="top:22px">The Book documents explained</h2>
  <div class="doc" style="left:30px"><i class="g"></i><i></i><i></i><i></i><i></i><i></i><i></i></div>
  <div class="doc" style="left:140px"><i class="g"></i><i></i><i></i><i></i><i></i><i></i><i></i></div>
  <div class="doc" style="left:250px"><i class="g"></i><i></i><i></i><i></i><i></i><i></i><i></i></div>
  <div class="doc" style="left:360px"><i class="g"></i><i></i><i></i><i></i><i></i><i></i><i></i></div>
  <div class="cap" style="left:30px;top:186px;width:96px">Box #1 title</div>
  <div class="cap" style="left:140px;top:186px;width:96px">Box #2 title</div>
  <div class="cap" style="left:250px;top:186px;width:96px">Box #3 title</div>
  <div class="cap" style="left:360px;top:186px;width:96px">Box #4 title</div>
</section>

<!-- 13 philanthropy -->
<section class="slide col-l r7">
  <div class="photo ph-sprout" style="left:260px;top:0;width:230px;height:240px" role="img" aria-label="Hands holding a young plant"></div>
  <div class="brand light">Marrowdale</div>
  <h2 class="title" style="left:24px;top:46px">Philanthropy</h2>
  <p class="body abs" style="left:24px;top:80px;width:215px">Charitable giving lets you support the causes you value while reducing the tax owed by your estate.</p>
  <p class="body abs" style="left:24px;top:122px;width:215px">We design gifting strategies that fit your family goals and leave a lasting mark on your community.</p>
  <div class="footer-rule"></div>
</section>

<!-- 14 savings -->
<section class="slide col-r r7">
  <div class="photo ph-warm" style="left:0;top:0;width:230px;height:240px" role="img" aria-label="Person reading by a warm lamp"></div>
  <div class="brand">Marrowdale</div>
  <h2 class="title" style="left:250px;top:46px">Savings</h2>
  <p class="body abs" style="left:250px;top:80px;width:215px">Steady saving over time is the root of a strong financial future for you and your family.</p>
  <p class="body abs" style="left:250px;top:122px;width:215px">We help you choose the right accounts and insurance tools to grow and protect what you save.</p>
  <div class="footer-rule"></div>
</section>

<!-- 15 transition of wealth -->
<section class="slide col-l r8">
  <div class="brand">Marrowdale</div>
  <h2 class="title center" style="top:22px;font-size:14px">The transition of wealth to the next generation</h2>
  <div class="item abs" style="left:30px;top:52px;width:134px"><h4>Write the option here</h4><p>Short text about this step.</p></div>
  <div class="item abs" style="left:178px;top:52px;width:134px"><h4>Write the option here</h4><p>Short text about this step.</p></div>
  <div class="item abs" style="left:326px;top:52px;width:134px"><h4>Write the option here</h4><p>Short text about this step.</p></div>
  <div class="photo ph-office" style="left:30px;top:110px;width:134px;height:60px" role="img" aria-label="Family meeting"></div>
  <div class="photo ph-lake" style="left:178px;top:110px;width:134px;height:60px" role="img" aria-label="Lake at dusk"></div>
  <div class="photo ph-forest" style="left:326px;top:110px;width:134px;height:60px" role="img" aria-label="Forest path"></div>
  <div class="item abs" style="left:30px;top:176px;width:134px"><h4>Write the option here</h4></div>
  <div class="item abs" style="left:178px;top:176px;width:134px"><h4>Write the option here</h4></div>
  <div class="item abs" style="left:326px;top:176px;width:134px"><h4>Write the option here</h4></div>
</section>

<!-- 16 legacy -->
<section class="slide col-r r8">
  <div class="brand">Marrowdale</div>
  <h2 class="title center" style="top:22px;font-size:14px">Building a legacy to continue long after you're gone</h2>
  <div class="bar" style="left:30px;top:56px;width:134px">Write the title here</div>
  <div class="bar" style="left:178px;top:56px;width:134px;background:var(--ink)">Write the title here</div>
  <div class="bar" style="left:326px;top:56px;width:134px">Write the title here</div>
  <p class="body abs" style="left:30px;top:80px;width:134px">Short text that explains this part of your legacy plan.</p>
  <p class="body abs" style="left:178px;top:80px;width:134px">Short text that explains this part of your legacy plan.</p>
  <p class="body abs" style="left:326px;top:80px;width:134px">Short text that explains this part of your legacy plan.</p>
  <div class="photo ph-sunset" style="left:30px;top:128px;width:134px;height:90px" role="img" aria-label="Sunset landscape"></div>
  <div class="photo ph-warm" style="left:178px;top:128px;width:134px;height:90px" role="img" aria-label="Grandparent with family"></div>
  <div class="photo ph-sprout" style="left:326px;top:128px;width:134px;height:90px" role="img" aria-label="Growing plant"></div>
</section>

</main>
</body>
</html>
```